Infection control

to re-design website to include the benefits of powdered bleach packed in pre-measured sachets which when dissolved in water provides economy, efficacy and is safe to use with the use of costly packaging. We need new text outlining the benefits of the world's most commonly used disinfectant for major hospitals, institutions, pathology, military and disaster areas.

Translate design into coded website using CMS with the following features:
Mobile responsive using HTML 5/ CSS3 standards
Coded with SEO standards and with H1 tags for easy spidering and with Wordpress CMS with is page rank 9
Site migration
Email support
Updates

Target Market(s)

hospitals, institutions, pathology, military and disaster areas

Industry/Entity Type

Chemical Product

Number of Pages Required

4 page

Colors

Designer to choose colors to be used in the design.

Requirements
Must have
• factual information based on the efficiency of sodium hypochlorite (bleach) used for infection control. The many viruses, bacteria, pathogens etc which certain strengths of bleach eliminate upon contact.
• As tis is a redesign, existing pages including MSDS sheets to stay the same
Nice to have
• a new look and feel including current logos
Should not have
• incorrect info

```html
<!DOCTYPE html>
<html lang="en">
<head>
<meta charset="utf-8">
<title>Contact Us – Clorana</title>
<link rel="stylesheet" href="https://fonts.googleapis.com/css2?family=Poppins:wght@400;500;600;700&display=swap">
<style>
:root{
  --green:#7cc242;
  --green-dark:#5fae1f;
  --hero:#8cc94f;
  --ink:#2b2b2b;
  --muted:#555;
  --line:#d9d9d9;
  --footer:#ececec;
  --white:#fff;
}
*{box-sizing:border-box;margin:0;padding:0}
html,body{width:811px;height:1200px;overflow:hidden;background:var(--white);font-family:'Poppins',sans-serif;color:var(--ink)}
.page{position:relative;width:811px;height:1200px}
.abs{position:absolute}
.brand{font-family:'Poppins',sans-serif;color:var(--green);font-weight:500;display:flex;align-items:center;gap:6px;line-height:1}
.brand .dot{border-radius:50%;background:var(--green);display:inline-block}
.tagline{font-size:9px;letter-spacing:.8px;color:var(--ink)}
.top-contact{display:flex;align-items:center;gap:8px;font-size:11px;color:var(--ink)}
.ring{width:25px;height:25px;border:2px solid var(--green);border-radius:50%;display:flex;align-items:center;justify-content:center}
.nav{display:flex;gap:17px;font-size:10.3px;font-weight:500;letter-spacing:.6px}
.nav a{color:var(--ink);text-decoration:none}
.nav a.active{color:var(--green)}
.header-line{top:81px;left:0;width:811px;height:1px;background:#e4e4e4}
.hero{top:82px;left:0;width:811px;height:255px;background:linear-gradient(90deg,#8fcb55,#86c64a 50%,#93cd5a)}
.hero h1{position:absolute;top:100px;width:100%;text-align:center;color:var(--white);font-size:30px;font-weight:700;letter-spacing:1px}
.intro{top:368px;left:66px;font-size:15px;font-weight:500}
.info-list{top:422px;left:66px;width:220px;font-size:10px;color:var(--ink)}
.info-item{display:flex;align-items:flex-start;gap:12px;margin-bottom:14px}
.info-item svg{flex:none}
.field{position:absolute;border:1px solid var(--line);box-shadow:inset 0 1px 2px rgba(0,0,0,.08);font-size:8px;font-style:italic;color:#777;padding:11px 11px}
.btn{position:absolute;background:var(--green);color:var(--white);font-size:10px;font-weight:600;display:flex;align-items:center;justify-content:center;letter-spacing:.3px}
.map{top:676px;left:0;width:811px;height:243px;background:linear-gradient(135deg,#e8ebe4,#dfe6d6 40%,#e9e9e6 70%,#dde8d0)}
.footer{top:919px;left:0;width:811px;height:226px;background:var(--footer)}
.footer h3{position:absolute;font-size:14.5px;font-weight:600;letter-spacing:.3px}
.f-field{position:absolute;background:var(--white);border:1px solid var(--line);font-size:7.5px;padding:10px 9px;color:var(--ink)}
.f-contact{font-size:8.6px;line-height:14px;color:var(--ink)}
.links{list-style:none;font-size:8px;line-height:15.2px}
.links li::before{content:"›";margin-right:10px}
.bottom{top:1145px;left:0;width:811px;height:55px;background:var(--white)}
.social{display:flex;gap:3px}
.social span{width:16px;height:16px;border:1px solid #444;border-radius:50%;display:block}
</style>
</head>
<body>
<div class="page">

  <!-- Header -->
  <header>
    <div class="abs brand" style="top:14px;left:66px;font-size:34px">
      <span class="dot" style="width:30px;height:30px"></span>Clorana
    </div>
    <div class="abs tagline" style="top:59px;left:68px">Hospital Grade Infection Control</div>

    <div class="abs top-contact" style="top:14px;left:431px">
      <span class="ring"><svg width="11" height="11" viewBox="0 0 24 24"><path fill="#7cc242" d="M6.6 10.8a15 15 0 0 0 6.6 6.6l2.2-2.2c.3-.3.7-.4 1-.2 1.1.4 2.3.6 3.6.6.6 0 1 .4 1 1V20c0 .6-.4 1-1 1A17 17 0 0 1 3 4c0-.6.4-1 1-1h3.5c.6 0 1 .4 1 1 0 1.3.2 2.5.6 3.6.1.3 0 .7-.2 1z"/></svg></span>1300 555 210
    </div>
    <div class="abs top-contact" style="top:14px;left:559px">
      <span class="ring"><svg width="11" height="9" viewBox="0 0 22 16"><rect x="1" y="1" width="20" height="14" rx="1.5" fill="none" stroke="#7cc242" stroke-width="2"/><path d="M1 2l10 7 10-7" fill="none" stroke="#7cc242" stroke-width="2"/></svg></span>info@cloranagroup.com
    </div>

    <nav class="abs nav" style="top:54px;left:295px">
      <a href="#">HOME</a><a href="#">ABOUT US</a><a href="#">PRODUCTS</a><a href="#">DOWNLOADS</a><a href="#">MEDIA &amp; NEWS</a><a class="active" href="#">CONTACT US</a>
    </nav>
    <div class="abs header-line"></div>
  </header>

  <!-- Hero -->
  <section class="abs hero" role="img" aria-label="Smiling medical staff in a hospital, tinted green">
    <h1>CONTACT US</h1>
    <svg class="abs" style="left:0;bottom:0" width="811" height="60" viewBox="0 0 811 60" preserveAspectRatio="none">
      <path d="M0 28 C120 -5 260 10 360 30 C520 55 680 60 811 30 L811 60 L0 60Z" fill="#fff"/>
      <path d="M0 30 C90 5 200 8 360 30 C200 12 90 18 0 44Z" fill="#6ebb2f"/>
    </svg>
  </section>

  <!-- Contact -->
  <main>
    <h2 class="abs intro">For more information or to order, contact:</h2>

    <div class="abs info-list">
      <div class="info-item">
        <svg width="14" height="18" viewBox="0 0 14 18"><path d="M7 0a7 7 0 0 0-7 7c0 5 7 11 7 11s7-6 7-11a7 7 0 0 0-7-7zm0 9.5A2.5 2.5 0 1 1 7 4.5a2.5 2.5 0 0 1 0 5z" fill="#2b2b2b"/></svg>
        <span style="line-height:14px">Clorana Bio Chemical Group Northfield,<br>Westbury, Kent</span>
      </div>
      <div class="info-item" style="align-items:center">
        <svg width="12" height="19" viewBox="0 0 12 19"><rect x="1" y="1" width="10" height="17" rx="2" fill="none" stroke="#2b2b2b" stroke-width="2"/><rect x="4" y="14" width="4" height="1.6" fill="#2b2b2b"/></svg>
        <span style="font-size:11px">Phone: 1300 555 210</span>
      </div>
      <div class="info-item" style="align-items:center">
        <svg width="16" height="12" viewBox="0 0 16 12"><rect width="16" height="12" rx="1" fill="#2b2b2b"/><path d="M0 1l8 6 8-6" fill="none" stroke="#fff" stroke-width="1.3"/></svg>
        <span>Email : info@cloranagroup.com</span>
      </div>
      <div class="info-item" style="align-items:center;margin-top:20px">
        <svg width="15" height="16" viewBox="0 0 15 16"><rect x="0" y="4" width="4" height="12" fill="#2b2b2b"/><rect x="5" y="0" width="10" height="16" fill="#2b2b2b"/><g fill="#fff"><rect x="7" y="8" width="2" height="2"/><rect x="11" y="8" width="2" height="2"/><rect x="7" y="12" width="2" height="2"/><rect x="11" y="12" width="2" height="2"/><rect x="7" y="2" width="6" height="3"/></g></svg>
        <span style="font-size:11px">Fax Direct: 1300 555 211</span>
      </div>
    </div>

    <div class="abs brand" style="top:563px;left:66px;font-size:30px">
      <span class="dot" style="width:26px;height:26px"></span>Clorana
    </div>
    <div class="abs tagline" style="top:604px;left:67px;font-size:8px">Hospital Grade Infection Control</div>

    <form>
      <div class="field" style="top:423px;left:308px;width:213px;height:27px">Your first name</div>
      <div class="field" style="top:423px;left:531px;width:214px;height:27px">Your email</div>
      <div class="field" style="top:458px;left:308px;width:213px;height:27px">Company Name</div>
      <div class="field" style="top:458px;left:531px;width:214px;height:27px">Your Phone</div>
      <div class="field" style="top:496px;left:308px;width:437px;height:71px">Message</div>
      <div class="btn" style="top:582px;left:309px;width:88px;height:24px">SUBMIT</div>
    </form>
  </main>

  <!-- Map -->
  <section class="abs map" role="img" aria-label="Street map showing the office location">
    <svg class="abs" style="left:395px;top:-12px" width="20" height="13" viewBox="0 0 20 13"><path d="M0 13L10 3 20 13Z" fill="#e8ebe4"/></svg>
    <svg class="abs" style="left:487px;top:97px" width="14" height="20" viewBox="0 0 14 20"><path d="M7 0a7 7 0 0 0-7 7c0 5 7 13 7 13s7-8 7-13a7 7 0 0 0-7-7z" fill="#e0403a"/><circle cx="7" cy="7" r="2.5" fill="#a11d18"/></svg>
  </section>

  <!-- Footer -->
  <footer class="abs footer">
    <h3 style="top:38px;left:66px">GET A QUICK NOW!</h3>
    <div class="f-field" style="top:81px;left:66px;width:153px;height:29px">Your Name</div>
    <div class="f-field" style="top:81px;left:228px;width:154px;height:29px">Your E - Mail</div>
    <div class="f-field" style="top:115px;left:66px;width:153px;height:29px">Your Phone</div>
    <div class="f-field" style="top:115px;left:228px;width:154px;height:29px">Message</div>
    <div class="btn" style="top:155px;left:66px;width:153px;height:27px">SUBMIT</div>

    <h3 style="top:38px;left:437px">CONTACT US</h3>
    <div class="abs f-contact" style="top:79px;left:437px">
      <div style="display:flex;gap:9px">
        <svg width="9" height="12" viewBox="0 0 14 18" style="margin-top:2px"><path d="M7 0a7 7 0 0 0-7 7c0 5 7 11 7 11s7-6 7-11a7 7 0 0 0-7-7zm0 9.5A2.5 2.5 0 1 1 7 4.5a2.5 2.5 0 0 1 0 5z" fill="#7cc242"/></svg>
        <span>Brightwell Supplies P.O. Box 4410<br>Fairhaven, CT 06500</span>
      </div>
      <div style="display:flex;gap:9px;margin-top:10px;font-size:9.5px">
        <svg width="10" height="10" viewBox="0 0 24 24" style="margin-top:2px"><path fill="#7cc242" d="M6.6 10.8a15 15 0 0 0 6.6 6.6l2.2-2.2c.3-.3.7-.4 1-.2 1.1.4 2.3.6 3.6.6.6 0 1 .4 1 1V20c0 .6-.4 1-1 1A17 17 0 0 1 3 4c0-.6.4-1 1-1h3.5c.6 0 1 .4 1 1 0 1.3.2 2.5.6 3.6.1.3 0 .7-.2 1z"/></svg>
        <span>Phone:1300 555 210<br>Fax : 1300 555 211</span>
      </div>
      <div style="display:flex;gap:10px;margin-top:6px">
        <svg width="9" height="7" viewBox="0 0 16 12" style="margin-top:4px"><rect width="16" height="12" fill="#7cc242"/><path d="M0 1l8 6 8-6" fill="none" stroke="#fff" stroke-width="1.3"/></svg>
        <span>info@cloranagroup.com</span>
      </div>
    </div>

    <h3 style="top:38px;left:635px">QUICK LINK</h3>
    <ul class="abs links" style="top:79px;left:636px">
      <li>Home</li><li>About</li><li>Products</li><li>Downloads</li><li>Media &amp; News</li><li>Contact Us</li>
    </ul>
  </footer>

  <!-- Bottom bar -->
  <div class="abs bottom">
    <div class="abs brand" style="top:13px;left:66px;font-size:17px;gap:4px">
      <span class="dot" style="width:15px;height:15px"></span>Clorana
    </div>
    <div class="abs" style="top:34px;left:67px;font-size:4.5px;letter-spacing:.3px">Hospital Grade Infection Control</div>
    <div class="abs" style="top:23px;left:340px;font-size:8px">©2018 Clorana. All Rights Reserved</div>
    <div class="abs social" style="top:22px;left:672px"><span></span><span></span><span></span><span></span></div>
    <div class="abs" style="top:25px;left:782px;font-size:7px;color:#888">C7</div>
  </div>

</div>
</body>
</html>
```